Prestige Car Bodyshop Business Card

We are a car bodyshop based in the UK. Our customer base is mainly prestige high-value vehicles. I am looking for a classy and stylish business card design for my staff to give out to customers, with their direct email and phone number, as well as our main email and phone number with address details

I am also looking to have a general business card design with just our main company address and contact details, but also have a space to add a manufacturer approval logo (i.e Velmora, Orek, Tovalo etc... logo) in the corner somewhere.

I do not particularly want any outlines or pictures of cars on the card, I would just like a quality high-end look.

Please feel free to get in touch if you have any questions or queries?

Many Thanks

Malcolm

Target Market(s)

Prestige vehicle owners

Industry/Entity Type

Automotive

Contact Information for Business Card

I am looking for a classy and stylish business card design for my staff to give out to customers, with their direct email and phone number, as well as our main email and phone number with address details

Font styles to use
Sans Serif

Colors

Designer to choose colors to be used in the design.

Requirements
Nice to have
• I do not particularly want any outlines or pictures of cars on the card, I would just like a quality high-end look.

```html
<!DOCTYPE html>
<html lang="en">
<head>
<meta charset="utf-8">
<title>Harwell Accident Repair Centre – Business Cards</title>
<link href="https://fonts.googleapis.com/css2?family=Lato:wght@400;700&display=swap" rel="stylesheet">
<style>
  :root{
    --stage:#1e1e1e;
    --card:#ffffff;
    --navy:#052c60;
    --navy-light:#0d4a94;
    --brand-blue:#0a4fa0;
    --orange:#f5821f;
    --ink:#333333;
  }
  *{margin:0;padding:0;box-sizing:border-box}
  html,body{width:1200px;height:900px;overflow:hidden;background:var(--stage)}
  body{position:relative;font-family:'Lato',sans-serif}
  .card{
    position:absolute;top:306px;width:440px;height:271px;
    background:var(--card);border-radius:10px;overflow:hidden;
    box-shadow:2px 3px 6px rgba(0,0,0,.55);
  }
  .card--front{left:149px}
  .card--back{left:608px}

  .header-band{
    position:absolute;left:0;top:0;width:100%;height:94px;
    background:linear-gradient(180deg,var(--navy-light) 0%,var(--navy) 100%);
  }
  .header-accent{
    position:absolute;right:0;top:0;width:98px;height:94px;
    background:var(--orange);
  }
  .brand-ring{
    position:absolute;left:283px;top:-7px;width:114px;height:114px;
    border-radius:50%;background:var(--card);
  }
  .brand-disc{
    position:absolute;border-radius:50%;
    background:radial-gradient(circle at 40% 30%,#1a66b8 0%,var(--brand-blue) 50%,var(--navy) 100%);
  }
  .card--front .brand-disc{left:300px;top:10px;width:80px;height:80px}
  .brand-name{
    position:absolute;font-weight:400;text-transform:uppercase;letter-spacing:.5px;line-height:1.2;
  }
  .card--front .brand-name{left:23px;top:22px;width:230px;color:#fff;font-size:21px}

  .staff-name{
    position:absolute;left:23px;top:116px;color:var(--brand-blue);
    font-size:16px;font-weight:700;text-transform:uppercase;
  }
  .contact-list{position:absolute;left:23px;list-style:none;font-size:12.5px;color:var(--ink)}
  .contact-list li{display:flex;align-items:center;height:17px}
  .contact-list svg{width:15px;height:15px;margin-right:5px;flex:none}
  .contact-list--direct{top:140px}
  .contact-list--office{top:224px}
  .address{
    position:absolute;left:23px;top:189px;font-size:12.5px;line-height:16px;color:var(--ink);
  }

  .card--back .brand-disc{left:90px;top:91px;width:88px;height:88px}
  .card--back .brand-name{left:190px;top:118px;color:var(--navy);font-size:22px;width:240px}
</style>
</head>
<body>
  <svg width="0" height="0" style="position:absolute" aria-hidden="true">
    <defs>
      <symbol id="icon-mobile" viewBox="0 0 16 16">
        <circle cx="8" cy="8" r="8" fill="#0a4fa0"/>
        <rect x="5.3" y="3.8" width="5.4" height="8.4" rx="1" fill="none" stroke="#fff" stroke-width="1.2"/>
      </symbol>
      <symbol id="icon-mail" viewBox="0 0 16 16">
        <circle cx="8" cy="8" r="8" fill="#0a4fa0"/>
        <rect x="4" y="5.2" width="8" height="5.6" fill="#fff"/>
        <path d="M4 5.4 8 8.4 12 5.4" fill="none" stroke="#0a4fa0" stroke-width="0.9"/>
      </symbol>
      <symbol id="icon-phone" viewBox="0 0 16 16">
        <circle cx="8" cy="8" r="8" fill="#0a4fa0"/>
        <path d="M5.2 4.2c.4-.3.9-.2 1.1.2l.8 1.4c.2.4.1.8-.2 1l-.5.4c.4.9 1.2 1.8 2.2 2.3l.4-.5c.3-.3.7-.4 1-.2l1.4.8c.4.2.5.7.2 1.1l-.6.8c-.4.5-1.1.6-1.7.3C7.1 10.8 5.3 9 4.4 6.8c-.3-.6-.1-1.3.3-1.7z" fill="#fff"/>
      </symbol>
    </defs>
  </svg>

  <section class="card card--front" aria-label="Staff business card, front">
    <div class="header-band"></div>
    <div class="header-accent"></div>
    <div class="brand-ring"></div>
    <div class="brand-disc"></div>
    <p class="brand-name">Harwell Accident Repair Centre</p>

    <h1 class="staff-name">Daniel Hartley</h1>
    <ul class="contact-list contact-list--direct">
      <li><svg><use href="#icon-mobile"/></svg>444 555 6688</li>
      <li><svg><use href="#icon-mail"/></svg>info@yourwebname.com</li>
    </ul>
    <p class="address">421, Address line here,<br>Dummy Code, 45452 Country Name</p>
    <ul class="contact-list contact-list--office">
      <li><svg><use href="#icon-phone"/></svg>888 555 4433</li>
      <li><svg><use href="#icon-mail"/></svg>info@companywebname.com</li>
    </ul>
  </section>

  <section class="card card--back" aria-label="Staff business card, back">
    <div class="brand-disc"></div>
    <p class="brand-name">Harwell Accident Repair Centre</p>
  </section>
</body>
</html>
```